Swimming Pool Business Billboard

10' x 24' Billboard displaying company name, logo and phone number. Picture of swimming pool activity; kids playing , swimming, etc. Bullet points possibly shown: New Construction, Repairs, Weekly maintenance.

Industry/Entity Type

Swimming pool construction, repairs and maintenance.

Font styles to use
Sans Serif

Colors
0054AA
0677BA
7BADD7
CADEEF
E8F1F8

Requirements
Must have
• Rusty & Calder Pembrook, RUSTY'S POOLS & Service,
Nice to have
• Prefer to have my last name "Pembrook" above the word "POOLS" only in smaller print so that "RUSTYS POOLS" is distinguished.

```html
<!DOCTYPE html>
<html lang="en">
<head>
<meta charset="UTF-8">
<title>Rusty's Pools & Service Billboard</title>
<link href="https://fonts.googleapis.com/css2?family=Poppins:wght@500;600;700;800&display=swap" rel="stylesheet">
<style>
  :root {
    --navy: #123f72;
    --brand-blue: #0054aa;
    --pool-blue: #0677ba;
    --sky: #7badd7;
    --pill: #b4d3ee;
    --pale: #cadeef;
    --mist: #e8f1f8;
    --white: #ffffff;
    --backdrop: #8f959d;
  }
  * { margin: 0; padding: 0; box-sizing: border-box; }
  html, body { width: 1200px; height: 1200px; overflow: hidden; }
  body {
    background: var(--backdrop);
    font-family: "Poppins", sans-serif;
    position: relative;
  }
  .billboard {
    position: absolute;
    left: 120px; top: 400px;
    width: 960px; height: 400px;
    background: var(--white);
    overflow: hidden;
  }
  .billboard-art { position: absolute; inset: 0; }
  .owners {
    position: absolute; left: 460px; width: 470px; top: 22px;
    text-align: center; color: var(--navy);
    font-weight: 700; font-size: 26px; line-height: 1;
  }
  .company-name {
    position: absolute; left: 460px; width: 470px; top: 80px;
    text-align: center; color: var(--white);
    font-weight: 700; font-size: 44px; line-height: 49px;
    letter-spacing: 0.2px;
  }
  .services {
    position: absolute; left: 452px; top: 200px; width: 480px;
    display: flex; justify-content: space-between;
  }
  .service {
    text-align: center; color: var(--navy);
    font-weight: 500; font-size: 19px; line-height: 24px;
  }
  .service svg { display: block; margin: 0 auto 4px; }
  .service-new { width: 160px; }
  .service-repairs { width: 100px; padding-top: 10px; }
  .service-weekly { width: 160px; }
  .phone-pill {
    position: absolute; left: 471px; top: 271px;
    width: 405px; height: 56px; border-radius: 28px;
    background: var(--pill);
    display: flex; align-items: center;
    padding-left: 6px;
  }
  .phone-icon {
    width: 46px; height: 46px; border-radius: 50%;
    background: var(--navy);
    display: flex; align-items: center; justify-content: center;
  }
  .phone-number {
    margin-left: 12px; color: var(--navy);
    font-weight: 700; font-size: 47px; letter-spacing: -0.5px; line-height: 1;
  }
  .contact {
    position: absolute; top: 366px; color: var(--white);
    font-weight: 500; font-size: 15.5px; line-height: 1;
    display: flex; align-items: center; gap: 5px;
  }
  .contact-address { left: 388px; }
  .contact-email { left: 738px; }
  .brand-seal {
    position: absolute; left: 312px; top: 56px;
    width: 144px; height: 144px; border-radius: 50%;
    background: var(--white);
    border: 5px solid var(--navy);
    display: flex; align-items: center; justify-content: center;
    text-align: center; color: var(--navy);
    font-weight: 700; font-size: 17px; line-height: 21px;
  }
</style>
</head>
<body>
  <main class="billboard">
    <svg class="billboard-art" width="960" height="400" viewBox="0 0 960 400">
      <defs>
        <linearGradient id="poolTones" x1="0" y1="0" x2="0" y2="1">
          <stop offset="0" stop-color="#6aa64a"/>
          <stop offset="0.08" stop-color="#d8d6cc"/>
          <stop offset="0.16" stop-color="#1d5fb8"/>
          <stop offset="0.6" stop-color="#2a71c4"/>
          <stop offset="0.82" stop-color="#cfe6ef"/>
          <stop offset="1" stop-color="#e6e6e0"/>
        </linearGradient>
      </defs>
      <rect class="title-band" x="0" y="70" width="960" height="117" fill="var(--navy)"/>
      <rect class="footer-band" x="0" y="318" width="960" height="82" fill="var(--navy)"/>
      <line x1="623" y1="224" x2="623" y2="269" stroke="#9aa3ad" stroke-width="1"/>
      <line x1="751" y1="224" x2="751" y2="269" stroke="#9aa3ad" stroke-width="1"/>
      <path class="pool-edge" d="M347,0 C395,60 425,150 418,221 C410,300 385,360 347,400" fill="none" stroke="var(--navy)" stroke-width="10"/>
      <path class="pool-photo" role="img" aria-label="Photo of a clear blue backyard swimming pool with steps and grass around it"
            d="M0,0 L347,0 C392,60 420,150 413,221 C405,300 380,360 344,400 L0,400 Z" fill="url(#poolTones)"/>
    </svg>

    <div class="brand-seal">RUSTY'S<br>POOLS</div>

    <p class="owners">Rusty &amp; Calder Pembrook</p>
    <h1 class="company-name">RUSTY'S POOLS<br>&amp; Service</h1>

    <ul class="services" style="list-style:none">
      <li class="service service-new">
        <svg width="15" height="15" viewBox="0 0 16 16"><circle cx="8" cy="8" r="8" fill="var(--navy)"/><path d="M4.5 8.3l2.3 2.2 4.7-4.7" fill="none" stroke="#fff" stroke-width="1.8"/></svg>
        New<br>Construction
      </li>
      <li class="service service-repairs">
        <svg width="15" height="15" viewBox="0 0 16 16"><circle cx="8" cy="8" r="8" fill="var(--navy)"/><path d="M4.5 8.3l2.3 2.2 4.7-4.7" fill="none" stroke="#fff" stroke-width="1.8"/></svg>
        Repairs
      </li>
      <li class="service service-weekly">
        <svg width="15" height="15" viewBox="0 0 16 16"><circle cx="8" cy="8" r="8" fill="var(--navy)"/><path d="M4.5 8.3l2.3 2.2 4.7-4.7" fill="none" stroke="#fff" stroke-width="1.8"/></svg>
        Weekly<br>maintenance
      </li>
    </ul>

    <div class="phone-pill">
      <span class="phone-icon">
        <svg width="26" height="26" viewBox="0 0 24 24"><path d="M6.6 10.8c1.4 2.8 3.8 5.1 6.6 6.6l2.2-2.2c.3-.3.7-.4 1-.2 1.1.4 2.3.6 3.6.6.6 0 1 .4 1 1V20c0 .6-.4 1-1 1C10.6 21 3 13.4 3 4c0-.6.4-1 1-1h3.5c.6 0 1 .4 1 1 0 1.3.2 2.5.6 3.6.1.3 0 .7-.2 1l-2.3 2.2z" fill="#fff"/></svg>
      </span>
      <span class="phone-number">912-555-0147</span>
    </div>

    <p class="contact contact-address">
      <svg width="11" height="13" viewBox="0 0 12 16"><path d="M6 0C2.7 0 0 2.6 0 5.9 0 10.3 6 16 6 16s6-5.7 6-10.1C12 2.6 9.3 0 6 0zm0 8.2a2.3 2.3 0 110-4.6 2.3 2.3 0 010 4.6z" fill="var(--pale)"/></svg>
      2750 Marlow Rd Brantley, GA 31599
    </p>
    <p class="contact contact-email">
      <svg width="13" height="10" viewBox="0 0 16 12"><rect width="16" height="12" rx="1" fill="var(--pale)"/><path d="M1 1l7 5 7-5" fill="none" stroke="var(--navy)" stroke-width="1.4"/></svg>
      rusty@rcpools.net
    </p>
  </main>
</body>
</html>
```